Orbit 528 - Pagevo Book Cover

I am looking for a Pagevo book cover for my book about "Orbit 528".
The Book is Titled:
Orbit 528 Advanced
Shaping Tomorrow: Paths Toward Unlocking Hidden Cosmic Laws
Author is Dorian Welby
Here is a book description that may help you understand more about it:
Inspired by the genius of Anton Brevik, this comprehensive guide delves into the ancient wisdom and cutting-edge science behind the 369 method, a powerful tool for manifesting your desires. Whether you're seeking personal growth, financial success, or spiritual enlightenment, this book provides advanced techniques and methods to transform your dreams into reality.
Any questions please ask.
Thanks
Colin

```html
<!DOCTYPE html>
<html lang="en">
<head>
<meta charset="UTF-8">
<title>Orbit 528 Advanced — Dorian Welby</title>
<link rel="stylesheet" href="https://fonts.googleapis.com/css2?family=Oswald:wght@400;500;600&family=Sacramento&family=Tinos&display=swap">
<style>
  :root {
    --sky-top: #120a2a;
    --sky-mid: #3a1f66;
    --violet: #6a3aa0;
    --horizon-pink: #e0507a;
    --horizon-orange: #f08a5d;
    --mountain: #3b2468;
    --ground: #0b0712;
    --peach: #f7dccf;
    --white: #ffffff;
    --slate: #9fb0c4;
  }
  html, body {
    margin: 0;
    padding: 0;
    width: 805px;
    height: 1200px;
    overflow: hidden;
    background: var(--ground);
  }
  .cover {
    position: relative;
    width: 805px;
    height: 1200px;
    overflow: hidden;
  }
  .cover-art {
    position: absolute;
    inset: 0;
    background:
      radial-gradient(ellipse 300px 300px at 50% 30%, rgba(230,170,230,0.45), rgba(140,80,190,0.18) 60%, transparent 75%),
      radial-gradient(ellipse 420px 90px at 50% 50%, rgba(240,120,110,0.55), transparent 80%),
      linear-gradient(180deg,
        var(--sky-top) 0%,
        var(--sky-mid) 22%,
        var(--violet) 38%,
        #8a3f8e 44%,
        var(--horizon-pink) 48%,
        var(--horizon-orange) 51%,
        #b04a86 55%,
        var(--mountain) 62%,
        #241546 75%,
        #140c26 88%,
        var(--ground) 100%);
  }
  .author {
    position: absolute;
    top: 20px;
    left: 0;
    width: 100%;
    margin: 0;
    text-align: center;
    font-family: "Oswald", sans-serif;
    font-weight: 500;
    font-size: 48px;
    line-height: 1.2;
    letter-spacing: 0.28em;
    text-indent: 0.28em;
    color: var(--peach);
  }
  .title {
    position: absolute;
    inset: 0;
    margin: 0;
    font-weight: normal;
    pointer-events: none;
  }
  .title-word,
  .title-number,
  .title-edition {
    position: absolute;
    left: 0;
    width: 100%;
    text-align: center;
    white-space: nowrap;
  }
  .title-word {
    top: 645px;
    font-family: "Oswald", sans-serif;
    font-weight: 500;
    font-size: 78px;
    line-height: 1;
    letter-spacing: 0.22em;
    text-indent: 0.22em;
    color: var(--peach);
  }
  .title-number {
    top: 760px;
    font-family: "Sacramento", cursive;
    font-size: 260px;
    line-height: 1;
    color: var(--peach);
    transform: scaleX(0.72);
    transform-origin: center;
  }
  .title-edition {
    top: 972px;
    font-family: "Oswald", sans-serif;
    font-weight: 500;
    font-size: 38px;
    line-height: 1;
    letter-spacing: 0.62em;
    text-indent: 0.62em;
    color: var(--white);
  }
  .subtitle {
    position: absolute;
    top: 1062px;
    left: 0;
    width: 100%;
    margin: 0;
    text-align: center;
  }
  .subtitle-lead {
    display: block;
    font-family: "Oswald", sans-serif;
    font-weight: 600;
    font-size: 19px;
    letter-spacing: 0.16em;
    color: var(--slate);
  }
  .subtitle-body {
    display: block;
    margin-top: 4px;
    font-family: "Tinos", serif;
    font-size: 21px;
    line-height: 1.12;
    color: var(--white);
  }
</style>
</head>
<body>
  <main class="cover">
    <div class="cover-art" role="img" aria-label="Starry violet night sky with a glowing sacred geometry circle above a sunset horizon and layered purple mountain ranges"></div>
    <p class="author">DORIAN WELBY</p>
    <h1 class="title">
      <span class="title-word">ORBIT</span>
      <span class="title-number">528</span>
      <span class="title-edition">ADVANCED</span>
    </h1>
    <p class="subtitle">
      <span class="subtitle-lead">SHAPING TOMORROW:</span>
      <span class="subtitle-body">Paths Toward Unlocking<br>Hidden Cosmic Laws</span>
    </p>
  </main>
</body>
</html>
```